Movie Poster Design for the Independent documentary, BEYOND NINE

We are seeking a compelling and provocative poster design for our first independent film, Beyond Nine. This is the story of Mason Fellick, a relentlessly positive young man facing the last year of his life after 7 years of living with a rare and incurable cancer, osteosarcoma. We need to take this poster with us to Brightwater next week where we can share our story with potential distributors and industry executives. We have applied to other festivals this is the first of the season and we hope to be selected for others.

Mason Fellick is an inspiration to almost anyone he meets, he's charming, funny, human and a generous soul who does what ever he can to help the next guy or the next kid. Mason wants pediatric cancer to stop with him and he does all he can with his days to do that and still have fun and enjoy life. We can all learn a lot from Mason. Be sure to watch our trailer, like us on Chatterly and give us an amazing design! Many images of Mason are available for download on our website. www.beyondnine-film.org - we also had a Fundmoor campaign and there are images there too. We've liked MG_7107.jpg best for promotional pieces so far.

We have used an image of Mason for postcards that feels similar to the image of "The Woman by the Lantern" and some on our team like it's simplicity but that design can be enhanced too. As the co-director I am open, I really want to see some fresh creativity on this and so I invite you to submit your best work.

One small note, Mason loves orange and we do to so if you can weave that in somehow that would be awesome. If you prefer to work with high rez images email me and I will send you a link to our full rez images.

As for poster text here is what we have written and some links to look at

BEYOND NINE Poster

http://www.layoutharbor.net/2011/02/7-elements-of-a-great-movie-poster-design/

Beyond Nine – Poster credits – one sheet size 27" × 40" and scalable to 7 x 11

Title - Beyond Nine

Chose a tag line

"It’s all about perspective"

"What would you do with the last year of your life?"

"Never, never give up"

---------------------
MOVIE POSTER FONT for credits
Steel Tong font - http://www.quillbarn4.net/2009/12/the-movie-poster-font-you-were-looking-for/

Larger Font

A Delvane Production
A film by co-directors
Rosalind Techter
Noor Delvane

Produced by
Noor Delvane
Rosalind Techter

Smaller font
Co Produced by

Tarik Bel-Haddou
Samir Bel-Haddou
Pruett Family
Walter Brindle
Marcia Brindle
Al Brindle
Nadine Brindle
Lavanya Osei
Herbert J. Vossel
Colette Vossel
Tammy Corvell
Greg Corvell
Wendling Family
Morgan Dalquist
Nathaniel Dalquist

Written by
Mason T. Fellick
Rosalind Techter

Directors of Photography

Benjamin Thorvald
Daniel Pemberlin

Editor
Daniel Pemberlin
Ilse Varno

Production Associate
Rob Kettleby

Original Music
Paul Marcovich

Larger font
Coming Soon
Or
Watch this with someone you love

*we know we have alot of co producers names, one option might be to cut them or to find a creative way to deal with them all.

Thank you and happy creating!
The Beyond Nine Team

Target Market(s)

Young adults and families

Industry/Entity Type

Industry

Font styles to use
Serif
Other font styles liked:
• open to suggestions

Colors
3176b5
faa54c
f79020
cfdeed
919191
7f7f7f
000000
333333
d3d3d3

Requirements
Must have
• Positivity and feel real and authentic
Nice to have
• some enhancements
Should not have
• should not be sleek, high tech or all graphics

```html
<!DOCTYPE html>
<html lang="en">
<head>
<meta charset="utf-8">
<title>Beyond Nine — One Sheet</title>
<link href="https://fonts.googleapis.com/css2?family=Oswald:wght@400;500;600&display=swap" rel="stylesheet">
<style>
  :root {
    --ink: #000000;
    --paper: #ffffff;
    --accent: #3176b5;
    --warm-light: #faa54c;
    --warm-deep: #f79020;
    --skin: #d9a07a;
    --skin-shadow: #5a3222;
  }
  * { margin: 0; padding: 0; box-sizing: border-box; }
  html, body {
    width: 948px;
    height: 1200px;
    overflow: hidden;
    background: var(--ink);
  }
  .poster {
    position: relative;
    width: 948px;
    height: 1200px;
    background: var(--ink);
    color: var(--paper);
    font-family: "Oswald", "Arial Narrow", sans-serif;
    text-transform: uppercase;
    overflow: hidden;
  }
  .portrait {
    position: absolute;
    left: 0;
    top: 250px;
    width: 760px;
    height: 950px;
    background:
      radial-gradient(ellipse 78% 80% at 38% 62%,
        var(--skin) 0%,
        color-mix(in srgb, var(--skin) 70%, var(--warm-deep)) 30%,
        var(--skin-shadow) 62%,
        var(--ink) 92%);
  }
  .portrait::after {
    content: "";
    position: absolute;
    inset: 0;
    background: linear-gradient(90deg, transparent 55%, var(--ink) 100%);
  }
  .warm-rule {
    position: absolute;
    right: 28px;
    top: 1040px;
    width: 120px;
    height: 4px;
    background: var(--warm-light);
  }
  .tagline {
    position: absolute;
    right: 28px;
    top: 50px;
    font-size: 31px;
    font-weight: 500;
  }
  .title {
    position: absolute;
    right: 24px;
    top: 76px;
    font-size: 150px;
    font-weight: 500;
    line-height: 1.1;
    letter-spacing: -2px;
  }
  .title .title-accent { color: var(--accent); }
  .credits-main {
    position: absolute;
    right: 28px;
    top: 428px;
    text-align: right;
    font-size: 20px;
    font-weight: 500;
    line-height: 29px;
  }
  .credits-main .label { color: var(--accent); }
  .credits-main .group + .group { margin-top: 24px; }
  .credits-block {
    position: absolute;
    right: 28px;
    top: 900px;
    width: 360px;
    text-align: justify;
    text-align-last: right;
    font-size: 11px;
    font-weight: 400;
    line-height: 17px;
  }
  .credits-block .role {
    color: var(--accent);
    font-size: 14px;
    font-weight: 500;
  }
  .sign-off {
    position: absolute;
    right: 28px;
    top: 1054px;
    text-align: right;
    font-size: 35px;
    font-weight: 500;
    line-height: 44px;
  }
  .sign-off .highlight { color: var(--accent); }
</style>
</head>
<body>
  <main class="poster">
    <div class="portrait" role="img" aria-label="Photograph of a young man with a shaved head and bare shoulders, looking back over his shoulder against a black background"></div>

    <p class="tagline">What would you do with the last year of your life?</p>
    <h1 class="title">Beyond<span class="title-accent">Nine</span></h1>

    <section class="credits-main">
      <div class="group">
        <p class="label">A Delvane Production</p>
        <p>A film by co-directors</p>
        <p>Rosalind Techter</p>
        <p>Noor Delvane</p>
      </div>
      <div class="group">
        <p class="label">Produced by</p>
        <p>Noor Delvane</p>
        <p>Rosalind Techter</p>
      </div>
    </section>

    <p class="credits-block">
      <span class="role">Written by</span> Mason T. Fellick · Rosalind Techter
      <span class="role">Directors of Photography</span> Benjamin Thorvald · Daniel Pemberlin
      <span class="role">Editor</span> Daniel Pemberlin · Ilse Varno
      <span class="role">Production Associate</span> Rob Kettleby
      <span class="role">Original Music</span> Paul Marcovich
      <span class="role">Co Produced by</span> Tarik Bel-Haddou · Samir Bel-Haddou · Pruett Family · Walter Brindle · Marcia Brindle · Al Brindle · Nadine Brindle · Lavanya Osei · Herbert J. Vossel · Colette Vossel · Tammy Corvell · Greg Corvell · Wendling Family · Morgan Dalquist · Nathaniel Dalquist
    </p>

    <p class="sign-off">Watch this with<br>someone <span class="highlight">you love</span></p>
  </main>
</body>
</html>
```